Microsite for a private healthcare provider

The design I need (PSD file) is for a company offering two services:
1. Recruitment of nurses
2. Provider a private health care: prenatal classes, vaccines for travellers
Here's a website we designed and we would like a similar style in terms of layout. Please note there will be about the same amount of content (text) http://lumeravisuel.example/fr
Main menu with 4 sections:
Accueil |Agence de placement | Soins privés | Contact
Links to their social media accounts:
https://twitter.com/Valdoriel
https://www.facebook.com/pages/Valdoriel-Agence-de-placement-en-soins-de-sant%C3%A9/482039571620413
Contact details:
TÉL. (555) 302-4419
TÉLEC. (555) 302-9154
1187 boulevard Ormelande, suite 3400
St-Hubert (Québec), K8W 5M3
Target Market(s)
Nurses looking for a job, Expecting women, People about to travel and seeking vaccines
Industry/Entity Type
Healthcare
Requirements
Must have
- 1- Must be responsive for mobiles and tablets
2 - Chirpline feed
3 - Google maps at the end next to their contact details
4- Two contact forms:
Form for people to send in their resume.
The form title is: Postulez
Fields required:
Nom complet
Courriel
Téléphone
Années d'expérience (with drop down list: 1-2 ans, 3-5 ans, 5 ans et plus)
Choose file (possibility to attach a cv)
Message
Form for requesting information
Form title is: Demande d'informations
Fields are:
Nom complet
Téléphone
Courriel
Message
Nice to have
- Here are some images on Pixvane Images the client likes, you can use for inspiration.
Agence de placement section:
File #40581936
File #6417283
File #8250946
File #5092734
File #47306152
File #39847201
File #26415037
Soins privés section:
File #33782519
File #31940285
File #34617092
File #48053276
File #27360458
File #29518064
File #42870315
File #6783052
File #35104827

```html
<!DOCTYPE html>
<html lang="fr">
<head>
<meta charset="utf-8">
<title>Valdoriel — Soins de santé personnalisés, en privé</title>
<link href="https://fonts.googleapis.com/css2?family=Roboto:wght@400;500;700&family=Ubuntu:wght@400;500;700&display=swap" rel="stylesheet">
<style>
:root{
  --green:#a6b823;
  --green-dark:#8e9e18;
  --ink:#2a2a2a;
  --nav:#2b2b2b;
  --footer:#2f2f2f;
  --sky:#00aeef;
  --orange:#e2631c;
  --muted:#8a8a8a;
  --line:#dcdcdc;
  --white:#ffffff;
}
*{box-sizing:border-box;margin:0;padding:0}
html,body{width:674px;height:1200px;overflow:hidden;background:var(--white)}
body{position:relative;font-family:"Roboto",Arial,sans-serif;color:var(--ink)}
.abs{position:absolute}
.brand{font-family:"Ubuntu",Arial,sans-serif;font-weight:700;color:var(--green);line-height:1}
.brand small{display:block;font-family:"Roboto",Arial,sans-serif;font-weight:400;font-size:5px;color:var(--white);margin-top:2px}

/* hero */
.hero{left:0;top:0;width:674px;height:238px;background:linear-gradient(90deg,#dfe6ea 0%,#c9d6dd 40%,#e8eef1 70%,#d5e0e6 100%)}
.hero-photo{left:130px;top:60px;width:240px;height:178px;background:radial-gradient(ellipse at 50% 40%,#7fa3c8 0%,#a9c2da 45%,rgba(210,222,230,0) 75%)}
.hero-brand{left:348px;top:62px;font-size:22px;color:#2a57a6}
.hero-brand small{color:#2a57a6;font-size:5.5px;font-style:normal}
.hero-copy{left:348px;top:104px;width:175px;font-size:7.3px;line-height:8.4px;color:#222}
.btn-learn{left:348px;top:157px;width:55px;height:17px;background:var(--ink);color:var(--white);font-size:6px;font-weight:500;padding:5px 0 0 5px;border-radius:1px}
.btn-learn i{position:absolute;right:5px;top:4px;width:9px;height:9px;border-radius:50%;background:var(--white)}
.dots{display:flex;gap:4px}
.dots span{width:8px;height:8px;border-radius:50%;background:#9c9c9c}
.dots span.on{background:var(--green)}

/* nav */
.nav{left:0;top:238px;width:674px;height:35px;background:var(--nav)}
.nav-brand{left:172px;top:9px;font-size:13px}
.nav-menu{left:305px;top:0;display:flex;list-style:none;height:35px}
.nav-menu li{font-size:5.6px;color:var(--white);padding:14px 7px 0;height:35px}
.nav-menu li.active{background:var(--green)}

/* agence */
.agence{left:0;top:273px;width:674px;height:197px;background:var(--green);color:var(--white)}
.sec-title{font-family:"Ubuntu",Arial,sans-serif;font-weight:500;font-size:11px;letter-spacing:.4px;text-align:center}
.agence-title{left:0;top:31px;width:674px}
.agence-lead{left:192px;top:59px;width:290px;font-size:6px;line-height:10px;text-align:center;color:#2d3208}
.portrait{left:197px;top:106px;width:68px;height:68px;border-radius:50%;border:2px solid #d7e07a;background:radial-gradient(circle at 50% 40%,#eef1f2 0%,#b9c6cf 70%)}
.agence-head{left:313px;top:107px;width:160px;font-size:6.3px;line-height:7.5px}
.agence-body{left:313px;top:130px;width:185px;font-size:4.1px;line-height:6.8px;color:#2d3208}
.agence-body p+p{margin-top:4px}

/* soins */
.tab{height:28px;width:161px;left:256px;background:var(--green);color:var(--white);font-family:"Ubuntu",Arial,sans-serif;font-weight:500;font-size:11px;text-align:center;padding-top:7px;letter-spacing:.4px}
.soins-tab{top:491px}
.vaccine{left:198px;top:551px;width:70px;height:70px;border-radius:50%;border:2px solid #e3e7ea;background:radial-gradient(circle at 50% 50%,#c4cfe3 0%,#e6ecf2 70%)}
.soins-title{left:313px;top:537px;font-size:11px;font-weight:500}
.soins-sub{left:313px;top:555px;font-size:7px;color:var(--orange)}
.soins-body{left:313px;top:576px;width:178px;font-size:4.1px;line-height:6.8px;color:#444}
.soins-body p+p{margin-top:4px}

/* contact */
.map{left:0;top:673px;width:674px;height:162px;background:linear-gradient(160deg,#ecebe6 0%,#e2e2da 50%,#ecebe6 100%)}
.contact-tab{top:696px}
.info{left:200px;top:779px;width:273px;height:49px;background:var(--green);color:var(--white)}
.info h4{font-size:6.2px;font-weight:400;margin-bottom:5px}
.info p{font-size:4px;line-height:10px}
.info .red{color:#c93a1a}
.social{display:flex;gap:6px;margin-top:3px}
.social span{width:13px;height:13px;border-radius:50%;border:1px solid var(--white)}

/* forms */
.form-title{font-size:11.5px;font-weight:500;color:#111}
.form-sub{font-size:4.4px;font-style:italic;color:var(--orange)}
.field{position:absolute;height:15px;border:1px solid var(--line);font-size:4.3px;color:#aaa;padding:5px 8px 0}
.btn-dark{position:absolute;height:14px;background:var(--ink);color:var(--white);font-size:7px;font-weight:700;text-align:center;padding-top:3px}
.opts{left:341px;top:956px;width:161px;height:40px;border:1px solid var(--line);border-top:0}
.opts div{height:10px;font-size:4.3px;color:#aaa;padding:3px 6px 0}
.opts .sel{background:var(--green);color:var(--white)}

/* twitter */
.feed{left:0;top:1039px;width:674px;height:77px;background:var(--sky);color:var(--white)}
.feed-disc{left:194px;top:14px;width:48px;height:48px;border-radius:50%;background:var(--white)}
.feed-name{left:257px;top:10px;font-family:"Ubuntu",Arial,sans-serif;font-weight:700;font-size:9px}
.feed-text{left:257px;top:28px;width:210px;font-size:4px;line-height:7.5px;color:#0b3c56}
.feed-text b{color:var(--white);font-weight:400}
.feed-meta{left:257px;top:57px;font-size:4px;color:#d4f0fc}
.feed-join{left:417px;top:57px;font-size:4px;color:var(--white);text-decoration:underline}

/* footer */
.footer{left:0;top:1116px;width:674px;height:84px;background:var(--footer)}
.fcol{position:absolute;top:16px;font-size:4px;color:#6e6e6e;line-height:6.5px}
.fcol h5{font-size:4.3px;font-weight:500;color:#9a9a9a;margin-bottom:4px;letter-spacing:.2px}
.copy{left:0;top:70px;width:674px;text-align:center;font-size:4px;color:#5e5e5e}
</style>
</head>
<body>

<section class="abs hero">
  <div class="abs hero-photo" role="img" aria-label="Photo de deux infirmières souriantes en blouse"></div>
  <div class="abs brand hero-brand">Valdoriel<small>Soins de santé personnalisés, en privé</small></div>
  <p class="abs hero-copy">Collaboratively administrate empowered markets via plug-and-play networks. Dynamically procrastinate B2C users after installed base benefits. Dramatically visualize customer directed convergence without revolutionary ROI.</p>
  <div class="abs btn-learn">Learn more<i></i>
    <svg class="abs" style="right:7px;top:7px" width="5" height="4" viewBox="0 0 5 4"><path d="M0 0h5L2.5 4z" fill="#2a2a2a"/></svg>
  </div>
  <div class="abs dots" style="left:467px;top:220px"><span class="on"></span><span></span><span></span></div>
</section>

<nav class="abs nav">
  <div class="abs brand nav-brand">Valdoriel<small>Soins de santé personnalisés, en privé</small></div>
  <ul class="abs nav-menu">
    <li class="active">ACCUEIL</li>
    <li>AGENCE DE PLACEMENT</li>
    <li>SOINS PRIVÉS</li>
    <li>CONTACT</li>
  </ul>
</nav>

<section class="abs agence">
  <h2 class="abs sec-title agence-title">AGENCE DE PLACEMENT</h2>
  <p class="abs agence-lead">Objectively innovate empowered manufactured products whereas parallel platforms. Holisticly predominate extensible testing procedures for reliable supply chains. Dramatically engage top-line web services vis-a-vis cutting-edge deliverables.</p>
  <div class="abs portrait" role="img" aria-label="Portrait d'un médecin avec stéthoscope"></div>
  <h3 class="abs agence-head" style="font-weight:400">Efficiently unleash cross-media information without cross-media value.</h3>
  <div class="abs agence-body">
    <p>Efficiently unleash cross-media information without cross-media value. Quickly maximize timely deliverables for real-time schemas. Dramatically maintain clicks-and-mortar solutions without functional solutions.</p>
    <p>Completely synergize resource sucking relationships via premier niche markets. Professionally cultivate one-to-one customer service with robust ideas.</p>
  </div>
</section>

<section>
  <h2 class="abs tab soins-tab">SOINS PRIVÉS</h2>
  <svg class="abs" style="left:156px;top:562px" width="12" height="36" viewBox="0 0 12 36"><path d="M11 1L1 18l10 17" fill="none" stroke="#9a9a9a" stroke-width=".8"/></svg>
  <svg class="abs" style="left:506px;top:562px" width="12" height="36" viewBox="0 0 12 36"><path d="M1 1l10 17L1 35" fill="none" stroke="#9a9a9a" stroke-width=".8"/></svg>
  <div class="abs vaccine" role="img" aria-label="Photo d'une vaccination au bras"></div>
  <h3 class="abs soins-title">Vaccines for Travellers</h3>
  <p class="abs soins-sub">Interactively procrastinate high-payoff content without.</p>
  <div class="abs soins-body">
    <p>Phosfluorescently engage worldwide methodologies with web-enabled technology. Interactively coordinate proactive e-commerce via process-centric "outside the box" thinking. Completely pursue scalable customer service through sustainable potentialities.</p>
    <p>Collaboratively administrate turnkey channels whereas virtual e-tailers. Objectively seize scalable metrics whereas proactive e-services. Seamlessly empower fully researched growth strategies and interoperable internal or "organic" sources.</p>
  </div>
  <div class="abs dots" style="left:313px;top:638px"><span class="on"></span><span></span></div>
</section>

<section>
  <div class="abs map" role="img" aria-label="Carte du quartier de St-Hubert avec l'emplacement du bureau"></div>
  <svg class="abs" style="left:381px;top:748px" width="16" height="22" viewBox="0 0 16 22"><path d="M8 21C3 14 1 11 1 8a7 7 0 0114 0c0 3-2 6-7 13z" fill="#c8201f"/><circle cx="8" cy="8" r="3" fill="#fff"/></svg>
  <h2 class="abs tab contact-tab">CONTACT</h2>
  <div class="abs info">
    <div class="abs" style="left:28px;top:6px">
      <h4>Valdoriel<span style="font-size:4px">.inc</span></h4>
      <p>1187 BOULEVARD ORMELANDE SUITE 3400<br>ST-HUBERT (QUÉBEC), K8W 5M3</p>
    </div>
    <div class="abs" style="left:133px;top:6px">
      <h4>PHONE</h4>
      <p>TEL: <span class="red">(555) 302-4419</span><br>TELEC: <span class="red">(555) 302-9154</span></p>
    </div>
    <div class="abs" style="left:196px;top:6px">
      <h4>Email</h4>
      <p class="red" style="line-height:6px">support@valdoriel.example</p>
      <div class="social"><span></span><span></span><span></span></div>
    </div>
  </div>
</section>

<section>
  <h2 class="abs form-title" style="left:170px;top:846px">Demande d'informations</h2>
  <p class="abs form-sub" style="left:172px;top:862px">Collaboratively administrate turnkey channels whereas virtual e-tailers.</p>
  <div class="field" style="left:171px;top:877px;width:163px">Nom complet</div>
  <div class="field" style="left:171px;top:898px;width:163px">Téléphone</div>
  <div class="field" style="left:171px;top:919px;width:163px">Courriel</div>
  <div class="field" style="left:171px;top:940px;width:163px;height:36px">Message</div>
  <div class="btn-dark" style="left:298px;top:983px;width:35px">SEND</div>

  <h2 class="abs form-title" style="left:341px;top:846px">Postulez</h2>
  <p class="abs form-sub" style="left:341px;top:862px">Objectively seize scalable metrics whereas proactive e-services.</p>
  <div class="field" style="left:341px;top:877px;width:161px">Nom complet</div>
  <div class="field" style="left:341px;top:899px;width:161px">Courriel</div>
  <div class="field" style="left:341px;top:920px;width:122px">Choose file</div>
  <div class="abs" style="left:469px;top:920px;width:33px;height:15px;background:var(--green);color:#fff;font-size:4px;text-align:center;padding-top:5px">Browse CV</div>
  <div class="field" style="left:341px;top:941px;width:161px">Années d'expérience</div>
  <div class="abs opts">
    <div class="sel">1-2 ans</div><div>3-5 ans</div><div>&gt;5 ans</div>
  </div>
  <div class="btn-dark" style="left:467px;top:1004px;width:35px">SUBMIT</div>
  <svg class="abs" style="left:532px;top:1017px" width="14" height="14" viewBox="0 0 14 14"><circle cx="7" cy="7" r="7" fill="#dfe4bf"/><path d="M4 9l3-4 3 4z" fill="#fff"/></svg>
  <span class="abs" style="left:549px;top:1021px;font-size:4px;color:#999">Go to top</span>
</section>

<section class="abs feed">
  <div class="abs feed-disc"></div>
  <h3 class="abs feed-name">Chirpline</h3>
  <p class="abs feed-text">valdoriel <b>@valdoriel</b><br>RT <b>@adminvaldo</b>: Collaboratively administrate turnkey channels whereas virtual e-tailers.<br>Objectively seize scalable metrics whereas. Web Design <b>http://vd.example/x</b> via <b>@studiobrume</b></p>
  <span class="abs feed-meta">1 hr 44 mins ago</span>
  <span class="abs feed-join">Join conversation</span>
</section>

<footer class="abs footer">
  <div class="fcol" style="left:172px"><h5>MAIN NAVIGATION</h5>Accueil<br>Agence De Placement<br>Soins Privés<br>Contact</div>
  <div class="fcol" style="left:249px"><h5>SECOND NAVIGATION</h5>About Us<br>Contact Us<br>Testimonials<br>Sitemap</div>
  <div class="fcol" style="left:322px"><h5>THIRD NAVIGATION</h5>About Us<br>Contact Us<br>Testimonials<br>Sitemap</div>
  <div class="fcol" style="left:395px"><h5>FOURTH NAVIGATION</h5>About Us<br>Contact Us<br>Testimonials<br>Sitemap</div>
  <div class="fcol" style="left:468px"><h5>LINK</h5>About Us<br>Contact Us<br>Testimonials<br>Sitemap</div>
  <p class="abs copy">© Copyright 2013 Valdoriel. All rights reserved</p>
</footer>

</body>
</html>
```